Branvique needs a business Card Design

We are looking for a business card Design for our new Managed Service Provider Company, Branvique. Branvique encompasses everything IT for the average medium sized business. Our primary services are help desk support, cyber-security (malware and ransomware protection), and Disaster Recovery systems. We would like the design to have a very clean and professional look, with a very minimalist feel.

Target Market(s)

Medium to large sized businesses

Industry/Entity Type

It Service

Contact Information for Business Card

Name GoesHere
name@branvique.com
O: 555-382-6047
C: 555-731-5820

Font styles to use
Other font styles liked:
• Poppins Font Only Please

Colors

Designer to choose only greyscale colors for use in the design.

Requirements
Must have
• Logo included
Nice to have
• Cutting Edge, innovative, minimalistic, elegant

```html
<!DOCTYPE html>
<html lang="en">
<head>
<meta charset="utf-8">
<title>Branvique Business Card</title>
<link href="https://fonts.googleapis.com/css2?family=Poppins:wght@400;500;600&display=swap" rel="stylesheet">
<style>
  :root {
    --page-bg: #efefef;
    --card-white: #ffffff;
    --ink-dark: #1e1e1e;
    --ink-soft: #3a3a3a;
  }
  * { margin: 0; padding: 0; box-sizing: border-box; }
  html, body {
    width: 1200px;
    height: 800px;
    overflow: hidden;
    background: var(--page-bg);
    font-family: "Poppins", sans-serif;
  }
  .canvas {
    position: relative;
    width: 1200px;
    height: 800px;
  }
  .card {
    position: absolute;
    width: 571px;
    height: 330px;
  }
  .card-front {
    left: 475px;
    top: 31px;
    background: var(--card-white);
    color: var(--ink-dark);
  }
  .card-back {
    left: 170px;
    top: 406px;
    background: var(--ink-dark);
    color: var(--card-white);
  }
  .brand-mark {
    position: absolute;
    background: var(--ink-dark);
  }
  .card-front .brand-mark {
    left: 412px;
    top: 68px;
    width: 24px;
    height: 24px;
  }
  .brand-name {
    position: absolute;
    font-weight: 400;
    line-height: 1;
    text-transform: uppercase;
    white-space: nowrap;
  }
  .card-front .brand-name {
    left: 424px;
    top: 132px;
    transform: translateX(-50%);
    font-size: 22px;
    letter-spacing: 6.5px;
    padding-left: 6.5px;
  }
  .card-back .brand-name {
    left: 258px;
    top: 243px;
    font-size: 34px;
    letter-spacing: 10px;
  }
  .card-back .brand-mark {
    left: 215px;
    top: 256px;
    width: 16px;
    height: 16px;
    background: var(--card-white);
  }
  .person {
    position: absolute;
    left: 44px;
    top: 143px;
  }
  .person-name {
    font-size: 18px;
    font-weight: 600;
    letter-spacing: 0.7px;
    text-transform: uppercase;
    line-height: 1.2;
  }
  .person-title {
    font-size: 14px;
    font-weight: 400;
    color: var(--ink-soft);
    line-height: 1.4;
  }
  .divider {
    width: 24px;
    height: 2px;
    background: var(--ink-dark);
    margin: 12px 0 11px;
  }
  .contact-list {
    list-style: none;
  }
  .contact-item {
    display: flex;
    align-items: center;
    gap: 7px;
    font-size: 15px;
    line-height: 20.5px;
    color: var(--ink-soft);
  }
  .contact-icon {
    width: 11px;
    height: 12px;
    flex: none;
    fill: var(--ink-dark);
  }
</style>
</head>
<body>
<main class="canvas">

  <section class="card card-front" aria-label="Business card front">
    <span class="brand-mark" aria-hidden="true"></span>
    <div class="brand-name">Branvique</div>

    <div class="person">
      <h1 class="person-name">Marcus Ellery</h1>
      <p class="person-title">Managing Director</p>
      <div class="divider"></div>
      <ul class="contact-list">
        <li class="contact-item">
          <svg class="contact-icon" viewBox="0 0 12 14" aria-hidden="true"><path d="M3 0h6a1.5 1.5 0 0 1 1.5 1.5v11A1.5 1.5 0 0 1 9 14H3a1.5 1.5 0 0 1-1.5-1.5v-11A1.5 1.5 0 0 1 3 0zm0 1.3a.3.3 0 0 0-.3.3V11h6.6V1.6a.3.3 0 0 0-.3-.3zM6 11.6a.8.8 0 1 0 0 1.6.8.8 0 0 0 0-1.6z"/></svg>
          555-382-6047
        </li>
        <li class="contact-item">
          <svg class="contact-icon" viewBox="0 0 14 14" aria-hidden="true"><path d="M3 0.5l2 3-1.2 1.5a8 8 0 0 0 5.2 5.2L10.5 9l3 2-1.2 2.3C6 13.5.5 8 .7 1.7z"/><path d="M8 1a5 5 0 0 1 5 5h-1.2A3.8 3.8 0 0 0 8 2.2zm0 2.3A2.7 2.7 0 0 1 10.7 6H9.5A1.5 1.5 0 0 0 8 4.5z"/></svg>
          555-731-5820
        </li>
        <li class="contact-item">
          <svg class="contact-icon" viewBox="0 0 14 14" aria-hidden="true"><path d="M1 3h12v8H1zm1.2 1.2L7 7.5l4.8-3.3z" fill-rule="evenodd"/></svg>
          name@branvique.com
        </li>
        <li class="contact-item">
          <svg class="contact-icon" viewBox="0 0 14 14" aria-hidden="true"><circle cx="7" cy="7" r="6"/><path d="M3 4.5c1.5 0 2 1 2.8 1.6.6.5.2 1.6-.6 1.8-.6.2-.5 1.3-.9 2.4M9.5 2.5c-.8.8-.2 1.7.5 2 .9.4 1.5.2 2.2 1.2" stroke="#fff" stroke-width="1" fill="none"/></svg>
          www.branvique.com
        </li>
      </ul>
    </div>
  </section>

  <section class="card card-back" aria-label="Business card back">
    <span class="brand-mark" aria-hidden="true"></span>
    <div class="brand-name">Branvique</div>
  </section>

</main>
</body>
</html>
```